Letterhead Design Project

I need letterhead designed for my law firm. It would also be used for web based stuff as well.

Industry/Entity Type

Law Firm

```html
<!DOCTYPE html>
<html lang="en">
<head>
<meta charset="utf-8">
<title>Hartwell &amp; Vance Law Firm – Letterhead</title>
<link rel="stylesheet" href="https://fonts.googleapis.com/css2?family=Source+Sans+3:wght@400;600&display=swap">
<style>
  :root {
    --paper: #ffffff;
    --ink-grey: #6a6a6a;
    --navy: #2b2672;
    --band: #2e2a7c;
    --photo-warm: #8a7a6e;
    --photo-cool: #5a4a48;
  }
  * { margin: 0; padding: 0; box-sizing: border-box; }
  html, body {
    width: 997px;
    height: 1200px;
    overflow: hidden;
    background: var(--paper);
  }
  .letterhead {
    position: relative;
    width: 997px;
    height: 1200px;
    background: var(--paper);
    font-family: "Source Sans 3", "Myriad Pro", Arial, sans-serif;
    color: var(--ink-grey);
  }
  .sender {
    position: absolute;
    left: 86px;
    top: 38px;
    font-size: 18px;
    line-height: 22px;
  }
  .sender__address { margin-top: 14px; }
  .firm-mark {
    position: absolute;
    left: 405px;
    top: 0;
    width: 184px;
    text-align: center;
  }
  .firm-mark__name {
    display: block;
    padding-top: 14px;
    font-size: 19px;
    font-weight: 600;
    line-height: 24px;
    color: var(--navy);
  }
  .firm-mark__photos {
    display: flex;
    justify-content: space-between;
    margin: 12px 14px 0;
  }
  .portrait {
    width: 68px;
    height: 78px;
  }
  .portrait--first { background: linear-gradient(160deg, var(--photo-warm), var(--photo-cool)); }
  .portrait--second { background: linear-gradient(160deg, #6a4a40, #3a2a2a); }
  .contact {
    position: absolute;
    left: 660px;
    top: 30px;
    list-style: none;
    font-size: 18px;
  }
  .contact__item {
    display: flex;
    align-items: center;
    gap: 12px;
    height: 30px;
  }
  .contact__badge {
    width: 20px;
    height: 20px;
    flex: none;
  }
  .footer-band {
    position: absolute;
    left: 0;
    bottom: 0;
    width: 100%;
    height: 20px;
    background: var(--band);
  }
</style>
</head>
<body>
<main class="letterhead">
  <address class="sender" style="font-style: normal;">
    <p class="sender__name">Name</p>
    <p class="sender__designation">Designation</p>
    <p class="sender__address">Address 01, ABC Street<br>XYZ lane, London , UK</p>
  </address>

  <header class="firm-mark">
    <span class="firm-mark__name">Hartwell &amp; Vance<br>Law Firm</span>
    <div class="firm-mark__photos">
      <div class="portrait portrait--first" role="img" aria-label="Portrait photo of the first partner"></div>
      <div class="portrait portrait--second" role="img" aria-label="Portrait photo of the second partner"></div>
    </div>
  </header>

  <ul class="contact">
    <li class="contact__item">
      <svg class="contact__badge" viewBox="0 0 20 20" aria-hidden="true">
        <circle cx="10" cy="10" r="10" fill="var(--navy)"/>
        <text x="10" y="14.5" text-anchor="middle" font-size="12" fill="#fff" font-family="Source Sans 3, sans-serif">P</text>
      </svg>
      <span>022 XXXXXXXXX</span>
    </li>
    <li class="contact__item">
      <svg class="contact__badge" viewBox="0 0 20 20" aria-hidden="true">
        <circle cx="10" cy="10" r="10" fill="var(--navy)"/>
        <text x="10" y="14.5" text-anchor="middle" font-size="12" fill="#fff" font-family="Source Sans 3, sans-serif">E</text>
      </svg>
      <span>name@websitename.com</span>
    </li>
    <li class="contact__item">
      <svg class="contact__badge" viewBox="0 0 20 20" aria-hidden="true">
        <circle cx="10" cy="10" r="10" fill="var(--navy)"/>
        <text x="10" y="14.5" text-anchor="middle" font-size="12" fill="#fff" font-family="Source Sans 3, sans-serif">W</text>
      </svg>
      <span>www.webname.com</span>
    </li>
  </ul>

  <div class="footer-band"></div>
</main>
</body>
</html>
```